Business Card Design - Corporate

Create a sleek elegant business card layout while suggesting a color scheme. Convey cutting edge technology while maintaining a corporate feel that is easily readable.

Company designs and manufactures consumer electronic products for mass retail that are mainly app driven.

(vector logo and die-line provided)

Target Market(s)

Corporate level, tech industry.

Industry/Entity Type

Business

Contact Information for Business Card

Generic Info:

Name
Title
email
address
phone 1
phone 2
website (vantorelle.com) on back

Font styles to use
Sans Serif

Requirements
Must have
• At least 2 colors + white on one side.
Nice to have
• Solid suggestion on color for logo and overall design. Color flood on back of card.
Should not have
• background texture like... marble, stone, patterns or circuit boards

```html
<!DOCTYPE html>
<html lang="en">
<head>
<meta charset="utf-8">
<title>Vantorelle Business Card</title>
<link rel="stylesheet" href="https://fonts.googleapis.com/css2?family=Montserrat:wght@500&family=Open+Sans:wght@400;600;700&display=swap">
<style>
  :root {
    --stage: #1c1c1f;
    --card: #232325;
    --card-edge: #2d2d30;
    --accent-blue: #1f7fd1;
    --text-light: #d9d9d9;
    --text-soft: #bdbdbd;
    --logo-grey: #8a8a8c;
    --logo-dark: #58585a;
    --page: #ffffff;
  }
  * { margin: 0; padding: 0; box-sizing: border-box; }
  html, body { width: 1200px; height: 1000px; overflow: hidden; background: var(--page); }
  .canvas { position: relative; width: 1200px; height: 1000px; }

  .stage {
    position: absolute; left: 0; top: 0; width: 1200px; height: 790px;
    background: var(--stage);
  }
  .card {
    position: absolute; top: 258px; width: 480px; height: 274px;
    background: var(--card);
    border: 1px solid var(--card-edge);
    border-radius: 3px;
    font-family: "Open Sans", Arial, sans-serif;
  }
  .card--front { left: 90px; }
  .card--back { left: 630px; display: flex; align-items: center; justify-content: center; }

  .identity {
    position: absolute; left: 40px; top: 86px; width: 170px; text-align: right;
  }
  .identity__name {
    color: var(--accent-blue); font-weight: 700; font-size: 19px; letter-spacing: 0.3px;
  }
  .identity__title {
    color: var(--text-light); font-weight: 600; font-size: 11px; letter-spacing: 0.5px; margin-top: 2px;
  }
  .divider {
    position: absolute; left: 224px; top: 64px; width: 1px; height: 84px; background: var(--accent-blue);
  }
  .contacts {
    position: absolute; left: 238px; top: 62px; list-style: none;
  }
  .contacts li {
    display: flex; align-items: center; gap: 8px;
    color: var(--text-light); font-size: 11.5px; line-height: 21px;
  }
  .contacts svg { width: 11px; height: 11px; fill: none; stroke: var(--accent-blue); stroke-width: 1.6; }
  .contacts .highlight { color: var(--accent-blue); }
  .address {
    position: absolute; right: 40px; bottom: 60px;
    color: var(--text-soft); font-size: 11.5px;
  }

  .wordmark {
    font-family: "Montserrat", Arial, sans-serif; font-weight: 500;
    letter-spacing: 6px; text-transform: uppercase;
  }
  .card--back .wordmark { color: var(--logo-grey); font-size: 40px; }

  .brand-band {
    position: absolute; left: 0; top: 790px; width: 1200px; height: 210px;
    display: flex; align-items: center; justify-content: center;
    background: var(--page);
  }
  .brand-band .wordmark { color: var(--logo-dark); font-size: 76px; letter-spacing: 10px; }
</style>
</head>
<body>
<main class="canvas">
  <section class="stage">
    <article class="card card--front">
      <div class="identity">
        <p class="identity__name">DANIEL REYES</p>
        <p class="identity__title">CEO/FOUNDER</p>
      </div>
      <div class="divider"></div>
      <ul class="contacts">
        <li>
          <svg viewBox="0 0 12 12"><path d="M3 1 L5 3.5 L4 5 Q5.5 7.5 7 8 L8.5 7 L11 9 L9.5 11 Q4 10.5 1 3 Z"/></svg>
          000 000 0000
        </li>
        <li>
          <svg viewBox="0 0 12 12"><rect x="3" y="1" width="6" height="10" rx="1"/></svg>
          000 000 0000
        </li>
        <li>
          <svg viewBox="0 0 12 12"><rect x="1" y="2.5" width="10" height="7"/><path d="M1 2.5 L6 6.5 L11 2.5"/></svg>
          info@danielreyes.com
        </li>
        <li>
          <svg viewBox="0 0 12 12"><circle cx="5" cy="5" r="3.5"/><path d="M7.5 7.5 L11 11"/></svg>
          <span>www.<span class="highlight">vantorelle</span>.com</span>
        </li>
      </ul>
      <p class="address">Your Street address, Singapore-1200</p>
    </article>

    <article class="card card--back">
      <span class="wordmark">Vantorelle</span>
    </article>
  </section>

  <footer class="brand-band">
    <span class="wordmark">Vantorelle</span>
  </footer>
</main>
</body>
</html>
```